Moodvane - Landing Page

Need a landing page for a journal app. The app is based on a retrospective board, where each journal entry is split into 3 sections: "What went well", "What Didn't Go Well" and "Things To Try".
The landing page should match the style of all modern web application landing pages. Think Plumo, Vexora, Zenquil. I've included screenshots of the app.
One feature that I want to highlight that is not ready yet, is an AI coach. It will offer insights based on the history of the user's journal entries
1 page

```html
<!DOCTYPE html>
<html lang="en">
<head>
<meta charset="utf-8">
<title>Moodvane – Structured Journaling</title>
<link href="https://fonts.googleapis.com/css2?family=Inter:wght@400;500;600&family=Poppins:ital,wght@0,500;0,600;0,700;1,600;1,700&display=swap" rel="stylesheet">
<style>
:root{
  --band:#0b55a9;
  --brand:#0d5aab;
  --bright:#1470ba;
  --pale:#e4edf7;
  --soft:#c7daee;
  --mid:#7ea5d3;
  --pattern-light:#dde7f3;
  --pattern-dark:#2a6bb8;
  --ink:#545454;
  --white:#ffffff;
  --device:#151515;
  --screen:#f3f5f8;
}
*{box-sizing:border-box;margin:0;padding:0}
html,body{width:1200px;height:3653px;overflow:hidden}
body{position:relative;background:var(--white);font-family:"Inter",sans-serif;color:var(--ink)}
.abs{position:absolute}
.heading{font-family:"Poppins",sans-serif}
em{font-style:italic;font-weight:700}

/* nav */
.logo{display:flex;align-items:center;gap:12px;font-family:"Poppins",sans-serif;font-weight:700;font-size:36px;color:var(--bright)}
.logo-mark{width:34px;height:44px;border-radius:7px;background:var(--soft)}
.nav{left:0;top:0;width:1200px;height:125px}
.nav-links{position:absolute;top:52px;left:648px;display:flex;gap:0;font-size:15px;font-weight:500;color:var(--brand)}
.nav-links span{position:absolute;white-space:nowrap}
.nav-divider{position:absolute;left:924px;top:52px;width:2px;height:22px;background:var(--mid)}
.btn{position:absolute;display:flex;align-items:center;justify-content:center;border-radius:6px;font-size:15px;font-weight:500}
.btn-solid{background:var(--brand);color:var(--white)}
.btn-outline{border:2px solid var(--white);color:var(--white)}

/* shared */
.pattern{position:absolute}
.pattern-light{background:var(--pattern-light)}
.pattern-dark{background:var(--pattern-dark)}
.book{position:absolute;background:var(--pale);clip-path:polygon(0 8%,50% 0,100% 8%,100% 100%,50% 92%,0 100%)}
.tile{position:absolute;border-radius:10px;background:var(--pale)}
.device{position:absolute;background:var(--device);border-radius:28px;padding:16px}
.device .screen{width:100%;height:100%;background:var(--screen);border-radius:14px}
.circle{position:absolute;border-radius:50%}

/* hero */
.hero-title{left:0;top:250px;width:1200px;text-align:center;font-size:41px;font-weight:600;color:var(--bright);letter-spacing:-.2px}
.hero-title em{color:var(--brand)}
.hero-sub{left:200px;top:324px;width:800px;text-align:center;font-size:20px;line-height:24px;color:var(--ink)}

/* about */
.band{position:absolute;left:0;width:1200px;background:var(--band);overflow:hidden}
.about-title{left:665px;top:938px;font-size:37px;font-weight:600;color:var(--white)}
.about-body{left:665px;top:1010px;width:440px;font-size:19.5px;line-height:24px;color:var(--white)}
.feature-icon{position:absolute;width:104px;height:104px;border-radius:50%;background:var(--mid)}

/* journals */
.journals-title{left:112px;top:1548px;width:420px;font-size:38px;line-height:57px;font-weight:600;color:var(--bright)}
.body-copy{font-size:20px;line-height:24px;color:#6a6a6a}
.body-copy strong{font-weight:600;color:#595959}
.tag{position:absolute;top:1451px;height:64px;border-radius:12px;background:var(--mid);display:flex;align-items:center;padding:0 20px;gap:14px;color:var(--white);font-style:italic;font-size:17px}
.tag svg{flex:none}

/* gym */
.gym-title{left:138px;top:2175px;font-size:37px;font-weight:600;color:var(--white)}
.track-title{left:752px;top:2216px;width:420px;font-size:38px;line-height:57px;font-weight:600;color:var(--bright)}

/* cta */
.cta-title{left:0;top:2858px;width:1200px;text-align:center;font-size:37px;line-height:57px;font-weight:600;color:var(--white)}
.cta-text{left:0;width:1200px;text-align:center;font-size:20px;color:var(--white)}
.cta-text a{color:var(--white);font-weight:700;font-style:italic;text-decoration:underline}

/* footer */
.footer-col{position:absolute;top:3300px}
.footer-col h4{font-family:"Poppins",sans-serif;font-size:20px;font-weight:600;color:var(--bright);margin-bottom:12px}
.footer-col li{list-style:none;font-size:16px;line-height:27px;color:#777}
.social{position:absolute;top:3342px;width:44px;height:44px;border-radius:50%;background:var(--mid)}
.bottom-bar{left:0;top:3575px;width:1200px;height:78px;background:#cfe0f2;border-top:2px solid var(--mid)}
.bottom-bar p{position:absolute;top:28px;font-size:15px;color:#555}
</style>
</head>
<body>

<!-- navigation -->
<header class="abs nav">
  <div class="abs logo" style="left:45px;top:38px"><span class="logo-mark"></span>Moodvane</div>
  <nav class="nav-links">
    <span style="left:0">Features</span>
    <span style="left:80px">Pricing</span>
    <span style="left:146px">Resources
      <svg width="18" height="10" viewBox="0 0 18 10" style="margin-left:8px"><path d="M1 1l8 7 8-7" fill="none" stroke="#0d5aab" stroke-width="1.8"/></svg></span>
  </nav>
  <span class="nav-divider"></span>
  <span class="abs" style="left:949px;top:52px;font-size:15px;font-weight:500;color:var(--brand)">Log in</span>
  <a class="btn btn-solid" style="left:1018px;top:41px;width:134px;height:41px">Start for free</a>
</header>

<!-- hero -->
<section>
  <div class="pattern pattern-light" role="img" aria-label="Light blue crosshatch pattern" style="left:0;top:125px;width:248px;height:247px"></div>
  <div class="tile" style="left:854px;top:180px;width:65px;height:65px"></div>
  <h1 class="abs heading hero-title">Transform Your <em>Reflections</em> Into <em>Growth</em></h1>
  <p class="abs hero-sub">Organize your thoughts with our structured journaling tool, and watch as your reflections turn into actionable insights.</p>
  <a class="btn btn-solid" style="left:533px;top:414px;width:134px;height:41px">Start for free</a>
  <div class="pattern pattern-light" role="img" aria-label="Light blue crosshatch pattern" style="left:950px;top:458px;width:250px;height:248px"></div>
  <div class="book" style="left:130px;top:518px;width:88px;height:56px"></div>
  <div class="device" style="left:238px;top:496px;width:724px;height:260px;border-radius:32px">
    <div class="screen" role="img" aria-label="App dashboard showing journal cards: Default Journal, Gym, Personal, Work"></div>
  </div>
</section>

<!-- about -->
<section class="band" style="top:706px;height:666px">
  <div class="circle" style="left:935px;top:-175px;width:370px;height:370px;background:var(--soft)"></div>
  <div class="abs" style="left:0;top:124px;width:617px;height:430px;background:var(--pale);border-top-right-radius:36px"></div>
  <div class="pattern" role="img" aria-label="Light blue crosshatch pattern" style="left:0;top:192px;width:305px;height:315px;background:#cbdcee"></div>
  <div class="book" style="left:52px;top:511px;width:68px;height:57px;background:#d4e2f1"></div>
  <div class="feature-icon" role="img" aria-label="Icon of a person climbing stairs" style="left:61px;top:79px"></div>
  <div class="feature-icon" role="img" aria-label="Icon of a presentation board" style="left:192px;top:79px"></div>
  <div class="feature-icon" role="img" aria-label="Icon of a growth bar chart" style="left:321px;top:79px"></div>
  <div class="feature-icon" style="left:450px;top:79px">
    <svg width="104" height="104" viewBox="0 0 104 104" fill="none" stroke="#fff" stroke-width="3">
      <rect x="28" y="30" width="12" height="12"/><rect x="28" y="47" width="12" height="12"/><rect x="28" y="64" width="12" height="12"/>
      <path d="M46 36h32M46 53h32M46 70h32"/>
    </svg>
  </div>
  <div class="device" style="left:119px;top:220px;width:511px;height:363px;border:2px solid #e6e6e6">
    <div class="screen" role="img" aria-label="Journal entry screen with three columns: What Went Well, What Didn't Go Well, Things To Try"></div>
  </div>
  <h2 class="abs heading about-title" style="top:232px">About Our <em>Journey</em></h2>
  <svg class="abs" style="left:1058px;top:209px" width="41" height="61" viewBox="0 0 41 61"><path d="M0 0h41v61L20.5 43 0 61z" fill="#fff"/></svg>
  <p class="abs about-body" style="top:304px">We set out to create a tool that goes beyond traditional journaling. Our app is designed to help you reflect on your experiences in a structured way, allowing you to clearly see what’s working in your life, what needs adjustment, and what new strategies you can try.</p>
  <a class="btn btn-outline" style="left:665px;top:515px;width:132px;height:40px">Learn More</a>
</section>

<!-- journals -->
<section class="abs" style="left:0;top:1372px;width:1200px;height:706px;overflow:hidden">
  <div class="circle" style="left:-147px;top:-185px;width:368px;height:368px;background:var(--soft)"></div>
  <div class="abs" style="left:587px;top:110px;width:613px;height:430px;background:var(--pale);border-radius:34px 0 0 34px"></div>
  <div class="tile" style="left:1113px;top:628px;width:65px;height:65px"></div>
</section>
<div class="tag" style="left:545px;width:200px">Default Journal
  <svg width="30" height="30" viewBox="0 0 30 30"><circle cx="15" cy="15" r="14" fill="#fff"/><path d="M8 15l5 5 9-10" fill="none" stroke="#7ea5d3" stroke-width="3"/></svg></div>
<div class="tag" style="left:755px;width:123px;justify-content:space-between">Gym
  <svg width="30" height="30" viewBox="0 0 30 30"><circle cx="15" cy="15" r="14" fill="#fff"/><path d="M8 15l5 5 9-10" fill="none" stroke="#7ea5d3" stroke-width="3"/></svg></div>
<div class="tag" style="left:888px;width:152px;justify-content:space-between">Personal
  <svg width="30" height="30" viewBox="0 0 30 30"><circle cx="15" cy="15" r="14" fill="#fff"/><path d="M8 15l5 5 9-10" fill="none" stroke="#7ea5d3" stroke-width="3"/></svg></div>
<div class="tag" style="left:1050px;width:127px;justify-content:space-between">Work
  <svg width="30" height="30" viewBox="0 0 30 30"><circle cx="15" cy="15" r="14" fill="#fff"/><path d="M8 15l5 5 9-10" fill="none" stroke="#7ea5d3" stroke-width="3"/></svg></div>
<h2 class="abs heading journals-title">Discover the Perfect Journal for <em>Every</em> <em>Aspect</em> of <em>Your Life</em></h2>
<p class="abs body-copy" style="left:112px;top:1737px;width:400px">Our app offers a variety of specialized journals to help you stay <strong>organized</strong> and <strong>focused</strong>, no matter where life takes you. Choose the journal that fits your needs and start your journey to <strong>self-improvement.</strong></p>
<a class="btn btn-solid" style="left:112px;top:1923px;width:133px;height:41px">Get Started</a>
<div class="device" style="left:662px;top:1552px;width:512px;height:363px">
  <div class="screen" role="img" aria-label="App dashboard with journal cards for Default Journal, Gym, Personal and Work"></div>
</div>

<!-- gym journal -->
<section class="abs" style="left:0;top:2078px;width:1200px;height:640px">
  <div class="abs" style="left:386px;top:79px;width:559px;height:545px;background:var(--pale);border-radius:36px"></div>
  <div class="abs" style="left:0;top:0;width:712px;height:536px;background:var(--band)"></div>
  <div class="pattern pattern-dark" role="img" aria-label="Blue crosshatch pattern" style="left:0;top:170px;width:227px;height:355px"></div>
  <div class="book" style="left:52px;top:511px;width:68px;height:58px"></div>
</section>
<h2 class="abs heading gym-title">Gym Journal</h2>
<span class="abs" style="left:404px;top:2196px;width:175px;height:3px;background:#fff"></span>
<div class="abs" role="img" aria-label="Line icon of a weightlifter" style="left:607px;top:2159px;width:68px;height:78px;background:#2a6bb8;border-radius:10px"></div>
<div class="device" style="left:123px;top:2299px;width:510px;height:363px;border:2px solid #e6e6e6">
  <div class="screen" role="img" aria-label="Gym journal timeline showing dated entries"></div>
</div>
<h2 class="abs heading track-title">Track your workouts, set goals, and monitor your progress.</h2>
<p class="abs body-copy" style="left:752px;top:2460px;width:400px">Lorem ipsum dolor sit amet, consectetur adipiscing elit. Sed do eiusmod tempor incididunt ut labore et dolore magna aliqua.</p>
<a class="btn btn-solid" style="left:752px;top:2598px;width:134px;height:40px">View More</a>

<!-- call to action -->
<section class="band" style="top:2780px;height:437px">
  <div class="pattern pattern-dark" role="img" aria-label="Blue crosshatch pattern" style="left:886px;top:0;width:314px;height:284px"></div>
  <div class="circle" style="left:-156px;top:270px;width:368px;height:368px;background:var(--soft)"></div>
  <div class="tile" style="left:31px;top:28px;width:65px;height:65px"></div>
  <div class="book" style="left:1081px;top:357px;width:86px;height:59px;background:#fff"></div>
</section>
<h2 class="abs heading cta-title">Take your reflections and growth with you,<br>wherever you go.</h2>
<p class="abs cta-text" style="top:2988px">Our app is available on all your favorite platforms.</p>
<p class="abs cta-text" style="top:3055px"><a>Download now</a> and start your journey to self-improvement.</p>
<a class="btn btn-outline" style="left:528px;top:3098px;width:144px;height:40px">Start for free</a>

<!-- footer -->
<footer>
  <div class="abs logo" style="left:71px;top:3303px"><span class="logo-mark"></span>Moodvane</div>
  <p class="abs" style="left:73px;top:3368px;width:280px;font-size:16px;line-height:19px;color:#666">Empowering you to grow through structured reflection and actionable insights.</p>
  <div class="footer-col" style="left:428px"><h4>Features</h4><ul><li>How It Works</li><li>For Teams</li><li>Pricing</li><li>Templates</li><li>Resources</li><li>Download App</li></ul></div>
  <div class="footer-col" style="left:596px"><h4>About Us</h4><ul><li>Our Story</li><li>Mission &amp; Vision</li><li>Blog</li><li>Careers</li></ul></div>
  <div class="footer-col" style="left:779px"><h4>Support</h4><ul><li>Help Center</li><li>FAQ</li><li>Contact Us</li><li>Privacy Policy</li><li>Terms of Service</li></ul></div>
  <div class="footer-col" style="left:963px"><h4>Stay Connected</h4></div>
  <span class="social" style="left:962px"></span>
  <span class="social" style="left:1015px"></span>
  <span class="social" style="left:1067px"></span>
  <span class="circle" style="left:74px;top:3566px;width:16px;height:16px;background:var(--brand)"></span>
  <span class="circle" style="left:99px;top:3566px;width:16px;height:16px;background:var(--brand)"></span>
  <span class="circle" style="left:124px;top:3566px;width:16px;height:16px;background:var(--brand)"></span>
  <div class="abs bottom-bar">
    <p style="left:73px">© 2024 <strong>Moodvane</strong>. All Rights Reserved.</p>
    <p style="right:74px">Privacy Policy | Terms of Service</p>
  </div>
</footer>

</body>
</html>
```